7KT Guided Signal: Caution - A book about Safety Messaging

Please refer to sample covers in the attached files none of which I found adequate.I would prefer a book cover that some kind of construction photo with people in it.
Book size is 6"*9"
“7KT Guided Signal: Caution” is a short book that is intended to provide some background and explanation in support of the 7KT Caution.com work site. The book is set up on Bristleway.com’s kindle site.
I would like to display the 7KT Caution logo, title, author name on the front cover with a suitable construction oriented photo in support of that. On the back cover I’d like to show if it makes sense the essence of 7KT Caution.com which is as follows:
7KT:
Right Messages,
Right People,
Right Time,
Right results
Prioritized
Proactive
Painless
Patented
7KT builds on the analysis of any process, near miss, accident, or incident and the subsequent repackaging of the resultant messages for delivery, audit and follow up on an ongoing basis. The messages and follow up are relentless and delivered before any subsequent events can occur. Specific and detailed messages from are managed; they are not forgotten. Quality is checked on a continuous basis.
A Safety Culture consists of the pool of ideas, thoughts, images, practices, written text, and beliefs that all constitute messages and guide our actions in the workplace. 7KT is designed to support existing practices and replace some of the less effective practices.
7KT simplifies the transmission of safety messages, information and ideas. Single messages will be easily handled and not lost in the sea of competing messages.
In its most simple form, a message is an idea a person either receives, or conceives and can communicate to another person. Messages include training, posters, hardhat stickers, safety manuals.
Updates
I would like to consider the following bylines for inclusion somewhere on the front or back cover of the book.Note that the book cover is designed to be used on PageLoom and so the cover will include the front and back of the book."The New Standard For Safety Messages Building a Culture of Confidence" Added Thursday, May 28, 2015
Target Market(s)
Safety Professionals worldwide
Industry/Entity Type
Construction
Requirements
Must have
- A back cover and be set up for Page Loom,
- The Title of the Book is 7KT Guided Signal: Caution
Nice to have
- A color construction Photo that spans back and front covers and comforms to the theme of the book.
- Tag lines that include:
- The New Standard in Safety Messaging
- Building a Culture of Confidence

```html
<!DOCTYPE html>
<html lang="en">
<head>
<meta charset="utf-8">
<title>7KT Guided Signal: Caution – Book Cover</title>
<link rel="stylesheet" href="https://fonts.googleapis.com/css2?family=Anton&family=Roboto+Condensed:ital,wght@0,300;0,400;0,700;1,700&display=swap">
<style>
  :root {
    --stage-dark: #2a1404;
    --stage-mid: #6a3a0c;
    --photo-amber: #e0892e;
    --photo-rust: #8a3f12;
    --photo-deep: #4a2109;
    --vest-cream: #e9dcae;
    --vest-khaki: #b59a5c;
    --hat-white: #f7efe2;
    --concrete: #cdbba8;
    --concrete-dark: #a8917a;
    --title-white: #ffffff;
    --title-yellow: #ffe21a;
    --title-orange: #f5a200;
    --brand-red: #c1272d;
    --ink: #2b2b2b;
    --ink-soft: #555555;
    --paper: #ffffff;
  }
  * { box-sizing: border-box; margin: 0; padding: 0; }
  html, body { width: 1200px; height: 1000px; overflow: hidden; }
  body {
    background: radial-gradient(ellipse at 50% 40%, var(--stage-mid) 0%, var(--stage-dark) 80%);
    font-family: "Roboto Condensed", "Arial Narrow", sans-serif;
    position: relative;
  }
  .cover {
    position: absolute;
    top: 95px;
    width: 540px;
    height: 810px;
    overflow: hidden;
    box-shadow: 0 12px 30px rgba(0,0,0,.5);
  }
  .cover--front { left: 40px; }
  .cover--back { left: 620px; background: var(--paper); }

  /* Front */
  .front-sky {
    position: absolute; inset: 0;
    background:
      linear-gradient(90deg, rgba(110,45,15,.75) 0%, rgba(110,45,15,0) 28%, rgba(110,45,15,0) 70%, rgba(110,45,15,.7) 100%),
      linear-gradient(180deg, #f0a040 0%, #e08a34 30%, #c9763a 55%, #9a5224 100%);
  }
  .front-workers {
    position: absolute; left: 0; right: 0; bottom: 0; height: 360px;
    background:
      radial-gradient(ellipse 120px 70px at 75% 18%, var(--hat-white) 0%, rgba(247,239,226,0) 100%),
      radial-gradient(ellipse 90px 55px at 30% 40%, var(--hat-white) 0%, rgba(247,239,226,0) 100%),
      linear-gradient(180deg, rgba(154,82,36,0) 0%, var(--vest-khaki) 45%, var(--vest-cream) 75%, var(--vest-khaki) 100%);
  }
  .brand {
    position: absolute;
    display: flex; align-items: center; gap: 8px;
    font-weight: 700;
    font-size: 20px;
    white-space: nowrap;
  }
  .brand__dot { width: 18px; height: 18px; border-radius: 50%; background: var(--brand-red); }
  .brand--front { top: 80px; left: 230px; color: var(--title-white); }
  .brand--back { top: 80px; right: 40px; color: var(--brand-red); }

  .front-title {
    position: absolute; top: 160px; left: 30px; right: 30px;
    text-align: right;
    transform: rotate(-3deg);
    transform-origin: right center;
  }
  .front-title__kicker {
    font-family: "Anton", sans-serif;
    color: var(--title-white);
    font-size: 40px;
    line-height: 1;
    text-shadow: 0 2px 3px rgba(0,0,0,.35);
  }
  .front-title__main {
    font-family: "Anton", sans-serif;
    font-size: 128px;
    line-height: .95;
    background: linear-gradient(180deg, var(--title-yellow) 30%, var(--title-orange) 100%);
    -webkit-background-clip: text; background-clip: text;
    color: transparent;
  }
  .front-author {
    position: absolute; top: 335px; right: 70px;
    color: var(--title-white);
    font-size: 16px;
    transform: rotate(-3deg);
  }

  /* Back */
  .back-photo {
    position: absolute; top: 0; right: 0; bottom: 0; width: 62%;
    background:
      linear-gradient(180deg, #f2c89a 0%, #f6dcc0 22%, var(--concrete) 55%, var(--concrete-dark) 100%);
  }
  .back-wash {
    position: absolute; inset: 0;
    background: linear-gradient(90deg, rgba(255,255,255,1) 0%, rgba(255,255,255,.92) 40%, rgba(255,255,255,.55) 70%, rgba(255,255,255,.2) 100%);
  }
  .back-content { position: absolute; top: 180px; left: 40px; right: 36px; }
  .pillars { display: flex; }
  .pillars__col { font-weight: 300; font-size: 22px; line-height: 1.2; color: var(--ink); }
  .pillars__col--left { padding-right: 22px; border-right: 1px dotted var(--ink-soft); }
  .pillars__col--right { padding-left: 22px; padding-top: 28px; }
  .pillars__label { color: var(--brand-red); font-weight: 400; font-size: 24px; }
  .tagline {
    margin-top: 30px;
    color: var(--brand-red);
    font-style: italic; font-weight: 700;
    font-size: 23px; line-height: 1.15;
  }
  .blurb {
    margin-top: 26px;
    column-count: 2; column-gap: 24px;
    font-size: 10.5px; line-height: 1.35;
    color: var(--ink);
  }
  .blurb p { margin-bottom: 12px; }
</style>
</head>
<body>
  <section class="cover cover--front">
    <div class="front-sky" role="img" aria-label="Photo of tall buildings under construction rising into an amber sky"></div>
    <div class="front-workers" role="img" aria-label="Photo of construction workers seen from behind in white hard hats and high-visibility vests, pointing up at the site"></div>
    <div class="brand brand--front"><span class="brand__dot"></span>7KT Caution</div>
    <h1 class="front-title">
      <span class="front-title__kicker">7KT GUIDED SIGNAL</span><br>
      <span class="front-title__main">CAUTION</span>
    </h1>
    <p class="front-author">Marcel Dufresne, P. Eng.</p>
  </section>

  <section class="cover cover--back">
    <div class="back-photo" role="img" aria-label="Faded photo of a tower crane and a concrete building under construction"></div>
    <div class="back-wash"></div>
    <div class="brand brand--back"><span class="brand__dot"></span>7KT Caution</div>
    <div class="back-content">
      <div class="pillars">
        <div class="pillars__col pillars__col--left">
          <div class="pillars__label">7KT:</div>
          Right Messages,<br>Right People,<br>Right Time,<br>Right results
        </div>
        <div class="pillars__col pillars__col--right">
          Prioritized<br>Proactive<br>Painless<br>Patented
        </div>
      </div>
      <h2 class="tagline">The New Standard For Safety<br>Messages Building a Culture<br>of Confidence</h2>
      <div class="blurb">
        <p>7KT builds on the analysis of any process, near miss, accident, or incident and the subsequent repackaging of the resultant messages for delivery, audit and follow up on an ongoing basis. The messages and follow up are relentless and delivered before any subsequent events can occur. Specific and detailed messages from are managed; they are not forgotten. Quality is checked on a continuous basis.</p>
        <p>A Safety Culture consists of the pool of ideas, thoughts, images, practices, written text, and beliefs that all constitute messages and guide our actions in the workplace. 7KT is designed to support existing practices and replace some of the less effective practices.</p>
        <p>7KT simplifies the transmission of safety messages, information and ideas. Single messages will be easily handled and not lost in the sea of competing messages.</p>
        <p>In its most simple form, a message is an idea a person either receives, or conceives and can communicate to another person. Messages include training, posters, hardhat stickers, safety manuals.</p>
      </div>
    </div>
  </section>
</body>
</html>
```